BRAVO New Zealand Summit 2020 - Wellington

A 1 x A4 Size Program booklet (4pg double-sided) designed for our upcoming event - BRAVO New Zealand Summit 2020, in Wellington New Zealand. We are seeking a fresh new style that is modern and sophisticated.

Content for the inside of the page will be provided later to the selected winner to update the program, the sponsor logo and the speaker photos.

Front cover:
Must have BRAVO Logo (See File 2 - 7 for logo variations free to use depending on design)
Topic: BRAVO New Zealand Summit 2020: Lifting the sourcing craft higher
Day and Date: Wednesday, 1 April 2020
Venue: Harbourgate Lodge, Wellington
CPD: 7hrs logo(see attachment file 13)

Inside Page 2, 3 and back page (Details to be provided after selecting winner)
The remaining 3 pages - You will need to have:
- 1 section for brief introduction (150 words approx)
- 1 section for sponsors logos to be featured
- 1 section of the Agenda/Program for the full day starting from 8am to 5pm
- 1 section for speaker photos

Target Market(s)

Procurement professionals, these are people who are responsible to buy for their organisation and organise contracts, they spend money in access of millions. It is targeting senior professional and highly qualified individuals.

Industry/Entity Type

Business

Font styles to use
Other font styles liked:
• Droid and Open Sans (See Branding guidelines)

Colors
00a990
33b8a4
86cfc6
e34197
e667a6
eea4c8
9bcb3b
add136
cadf82

Requirements
Must have
• - See File 1 - Branding Guidelines (for font, colour and image selection guidance)
• - See File 10,11 & 12 example of our Case Studies to have an idea but do not replicate this. As this is a conference, we want something fresh and so you are open to change the layout style within these branding guidelines.
• - See File 8 & 9 - Must use our official Fonts - Droid & Open sans
Nice to have
• Find something that suits the conference theme for procurement professional rising in their career or moving into the future. You can also feature Wellington city but this could be a bit boring. It is important to sticks to our branding guideline.
• Remember our font is Droid-Serif for headings and italised and Open-Sans for sub-headings.
Should not have
• See Branding guideline document

```html
<!DOCTYPE html>
<html lang="en">
<head>
<meta charset="utf-8">
<title>BRAVO New Zealand Summit 2020 – Program Spread</title>
<link rel="stylesheet" href="https://fonts.googleapis.com/css2?family=Open+Sans:wdth,wght@75..100,300..800&display=swap">
<style>
  :root {
    --canvas: #e9e9e9;
    --header-dark: #0d1a3a;
    --header-mid: #10506a;
    --header-teal: #1c8f9a;
    --pink-page: #f8d9e8;
    --pink-strong: #e34197;
    --pink-mid: #e667a6;
    --pink-soft: #eea4c8;
    --pink-pale: #f4c4da;
    --teal-page: #1fab8f;
    --ink: #1a1a1a;
    --white: #ffffff;
  }
  * { box-sizing: border-box; margin: 0; padding: 0; }
  html, body {
    width: 1170px; height: 1200px; overflow: hidden;
    background: var(--canvas);
    font-family: "Open Sans", Arial, sans-serif;
  }
  .spread {
    position: absolute; left: 94px; top: 231px;
    width: 980px; height: 692px;
    background: var(--pink-page);
    box-shadow: 0 6px 18px rgba(0,0,0,.25);
    overflow: hidden;
  }
  .page-left { position: absolute; left: 0; top: 0; width: 490px; height: 692px; background: var(--pink-page); }
  .page-right { position: absolute; left: 490px; top: 0; width: 490px; height: 692px; background: var(--teal-page); }

  .masthead {
    position: absolute; left: 0; top: 0; width: 980px; height: 110px;
    background:
      radial-gradient(ellipse 260px 90px at 560px 40px, rgba(120,220,220,.45), transparent 70%),
      radial-gradient(ellipse 300px 120px at 250px 30px, rgba(40,150,170,.55), transparent 70%),
      linear-gradient(90deg, var(--header-dark) 0%, var(--header-mid) 35%, var(--header-teal) 55%, var(--header-mid) 75%, var(--header-dark) 100%);
  }
  .masthead-rule { position: absolute; left: 147px; top: 83px; width: 805px; height: 1px; background: rgba(255,255,255,.6); }

  .brand { position: absolute; left: 21px; top: 19px; color: var(--white); }
  .brand-mark { position: absolute; left: 0; top: 0; width: 46px; height: 46px; border-radius: 50%; background: var(--white); }
  .brand-name { position: absolute; left: 52px; top: -5px; font-size: 44px; font-weight: 800; letter-spacing: -.5px; line-height: 1; }
  .brand-sub { position: absolute; left: 53px; top: 42px; font-size: 12px; font-weight: 700; line-height: 12px; white-space: nowrap; }

  .city-photo {
    position: absolute; left: 369px; top: 0; width: 101px; height: 128px;
    background: linear-gradient(180deg, #7fa6c9 0%, #9bb8cf 25%, #6f8ea3 45%, #8a8f86 60%, #3e6b33 85%, #2d5a2a 100%);
    box-shadow: 0 3px 6px rgba(0,0,0,.35);
  }

  .headline {
    position: absolute; right: 28px; top: 22px; text-align: right; color: var(--white);
    font-stretch: 75%; font-weight: 300; font-size: 30px; line-height: 28px;
  }
  .event-meta {
    position: absolute; right: 29px; top: 86px; color: var(--white);
    font-size: 7px; font-weight: 700; white-space: nowrap;
  }
  .event-meta .sep { display: inline-block; width: 1px; height: 9px; background: rgba(255,255,255,.7); margin: 0 8px; vertical-align: -2px; }

  .section-tab { position: absolute; top: 108px; height: 22px; }
  .section-tab svg { position: absolute; left: 0; top: 0; }
  .section-tab span {
    position: relative; display: block; color: var(--white);
    font-size: 12.5px; font-weight: 800; padding-top: 1px; white-space: nowrap;
  }
  .tab-agenda { left: 34px; width: 160px; }
  .tab-agenda span { padding-left: 15px; }
  .tab-speakers { left: 526px; width: 130px; }
  .tab-speakers span { padding-left: 35px; }

  .agenda {
    position: absolute; left: 32px; top: 147px; width: 429px; height: 510px;
    border-radius: 14px; overflow: hidden; background: var(--pink-strong);
  }
  .agenda-row { display: flex; height: 49px; }
  .agenda-time {
    width: 93px; padding-left: 24px; font-size: 16px; color: var(--white);
    display: flex; align-items: center;
  }
  .agenda-item {
    flex: 1; padding-left: 28px; font-size: 12.5px; color: var(--ink);
    display: flex; align-items: center; letter-spacing: .3px;
  }
  .agenda-row.strong .agenda-time { background: var(--pink-strong); }
  .agenda-row.strong .agenda-item { background: var(--pink-soft); }
  .agenda-row.soft .agenda-time { background: var(--pink-mid); }
  .agenda-row.soft .agenda-item { background: var(--pink-pale); }
  .agenda-row:first-child .agenda-item { box-shadow: inset 0 -1px 0 #b96a8e; }
  .agenda-note { display: flex; height: 20px; }
  .agenda-note .agenda-time { background: var(--pink-strong); }
  .agenda-note .agenda-item { background: var(--pink-pale); font-size: 5.5px; align-items: flex-start; padding-top: 3px; }

  .speakers { position: absolute; left: 552px; top: 167px; width: 410px; }
  .speaker { position: relative; height: 127px; width: 410px; }
  .speaker-photo { position: absolute; left: 0; top: 0; width: 99px; height: 100px; }
  .speaker-info { position: absolute; left: 119px; top: 1px; color: var(--white); }
  .speaker-name { font-size: 12.5px; line-height: 16px; padding-left: 3px; }
  .speaker-title { font-size: 12.5px; line-height: 16px; }
  .speaker-bio { font-size: 11px; line-height: 16.3px; letter-spacing: .9px; white-space: nowrap; }

  .folio {
    position: absolute; top: 664px; font-size: 7px; font-weight: 700; font-stretch: 75%;
    color: var(--ink); white-space: nowrap; display: flex; align-items: center;
  }
  .folio .sep { display: inline-block; width: 1px; height: 14px; margin: 0 9px; }
  .folio-left { left: 22px; }
  .folio-left .sep { background: var(--ink); }
  .folio-right { right: 22px; color: var(--white); }
  .folio-right .sep { background: var(--white); }
</style>
</head>
<body>
<main class="spread">
  <section class="page-left"></section>
  <section class="page-right"></section>

  <header class="masthead">
    <div class="masthead-rule"></div>
    <div class="brand">
      <div class="brand-mark"></div>
      <div class="brand-name">BRAVO</div>
      <div class="brand-sub">New Zealand<br>Summit<br>2020</div>
    </div>
    <div class="headline">Lifting the sourcing<br>craft higher</div>
    <div class="event-meta">Wednesday 1 April 2020<span class="sep"></span>Harbourgate Lodge, Wellington</div>
  </header>

  <div class="city-photo" role="img" aria-label="Photo of Wellington harbour and city buildings"></div>

  <div class="section-tab tab-agenda">
    <svg width="160" height="22" viewBox="0 0 160 22" aria-hidden="true">
      <path d="M0 0 L10 18 Q12 21 16 21 L142 21 Q146 21 148 18 L158 0 Z" fill="#0d1a3a" stroke="#ffffff" stroke-width="1.2"/>
    </svg>
    <span>AGENDA | PROGRAM</span>
  </div>

  <div class="section-tab tab-speakers">
    <svg width="130" height="22" viewBox="0 0 130 22" aria-hidden="true">
      <path d="M0 0 L10 18 Q12 21 16 21 L112 21 Q116 21 118 18 L128 0 Z" fill="#0d1a3a" stroke="#ffffff" stroke-width="1.2"/>
    </svg>
    <span>SPEAKERS</span>
  </div>

  <div class="agenda">
    <div class="agenda-row strong"><div class="agenda-time">8am</div><div class="agenda-item">XXXXXXXXXXXXXXXXXXX</div></div>
    <div class="agenda-row soft"><div class="agenda-time">9am</div><div class="agenda-item">XXXXXXXXXXXXXXXXXXXXXX</div></div>
    <div class="agenda-row strong"><div class="agenda-time">10am</div><div class="agenda-item">XXXXXXXXXXXXXXXXXXXXXXXX</div></div>
    <div class="agenda-row soft"><div class="agenda-time">11am</div><div class="agenda-item">XXXXXXXXXX</div></div>
    <div class="agenda-row strong"><div class="agenda-time">12pm</div><div class="agenda-item">XXXXXXXXXXXXXXXXXX</div></div>
    <div class="agenda-row soft"><div class="agenda-time">1pm</div><div class="agenda-item">XXXXXXXXXXXXXXXXXXXXXXXX</div></div>
    <div class="agenda-row strong"><div class="agenda-time">2pm</div><div class="agenda-item">XXXXXXXXXXXXXXXXXXXXX</div></div>
    <div class="agenda-row soft"><div class="agenda-time">3pm</div><div class="agenda-item">XXXXXXXXXXXXXXXX</div></div>
    <div class="agenda-row strong"><div class="agenda-time">4pm</div><div class="agenda-item">XXXXXXXXXXXXXXXXXX</div></div>
    <div class="agenda-row soft"><div class="agenda-time">5pm</div><div class="agenda-item">XXXXXXXXXXXXXXXXXXXXXXXX</div></div>
    <div class="agenda-note"><div class="agenda-time"></div><div class="agenda-item">• XXXXXXXXXXXXXXXXXXXXXXXXXXXXXXXXXXXXXXXXXXXXX</div></div>
  </div>

  <div class="speakers">
    <article class="speaker">
      <div class="speaker-photo" role="img" aria-label="Speaker portrait photo" style="background:linear-gradient(180deg,#8c9aa6 0%,#b9b3ab 45%,#1f2d4a 80%,#16223a 100%)"></div>
      <div class="speaker-info">
        <div class="speaker-name">Name Surname</div>
        <div class="speaker-title">Title</div>
        <div class="speaker-bio">xxxxxxxxxxxxxxxxxxxxxxxxxxxxxxxxxxxxxxxxx<br>xxxxxxxxxxxxxxxxxxxxxxxxxxxxxxxxxxxxxxxxxxx<br>xxxxxxxxxxxxxxxxxxxxxxxxxxxxxxxxxxxxxxxxx<br>xxxxxxxxxxxxxxxxxxxxxxxxxxxxxxxxxxxxxxxxxx</div>
      </div>
    </article>
    <article class="speaker">
      <div class="speaker-photo" role="img" aria-label="Speaker portrait photo" style="background:linear-gradient(180deg,#dcdcdc 0%,#c69a80 40%,#2b3546 75%,#1c2533 100%)"></div>
      <div class="speaker-info">
        <div class="speaker-name">Name Surname</div>
        <div class="speaker-title">Title</div>
        <div class="speaker-bio">xxxxxxxxxxxxxxxxxxxxxxxxxxxxxxxxxxxxxxxxx<br>xxxxxxxxxxxxxxxxxxxxxxxxxxxxxxxxxxxxxxxxxxx<br>xxxxxxxxxxxxxxxxxxxxxxxxxxxxxxxxxxxxxxxxx<br>xxxxxxxxxxxxxxxxxxxxxxxxxxxxxxxxxxxxxxxxxx</div>
      </div>
    </article>
    <article class="speaker">
      <div class="speaker-photo" role="img" aria-label="Speaker portrait photo" style="background:linear-gradient(180deg,#f2f2f2 0%,#2a1e1a 30%,#b98a72 55%,#3a8fd0 100%)"></div>
      <div class="speaker-info">
        <div class="speaker-name">Name Surname</div>
        <div class="speaker-title">Title</div>
        <div class="speaker-bio">xxxxxxxxxxxxxxxxxxxxxxxxxxxxxxxxxxxxxxxxx<br>xxxxxxxxxxxxxxxxxxxxxxxxxxxxxxxxxxxxxxxxxxx<br>xxxxxxxxxxxxxxxxxxxxxxxxxxxxxxxxxxxxxxxxx<br>xxxxxxxxxxxxxxxxxxxxxxxxxxxxxxxxxxxxxxxxxx</div>
      </div>
    </article>
    <article class="speaker">
      <div class="speaker-photo" role="img" aria-label="Speaker portrait photo" style="background:linear-gradient(180deg,#e9ece8 0%,#b78a66 35%,#d9b49a 60%,#f3f3f0 100%)"></div>
      <div class="speaker-info">
        <div class="speaker-name">Name Surname</div>
        <div class="speaker-title">Title</div>
        <div class="speaker-bio">xxxxxxxxxxxxxxxxxxxxxxxxxxxxxxxxxxxxxxxxx<br>xxxxxxxxxxxxxxxxxxxxxxxxxxxxxxxxxxxxxxxxxxx<br>xxxxxxxxxxxxxxxxxxxxxxxxxxxxxxxxxxxxxxxxx<br>xxxxxxxxxxxxxxxxxxxxxxxxxxxxxxxxxxxxxxxxxx</div>
      </div>
    </article>
  </div>

  <footer class="folio folio-left">2<span class="sep"></span>BRAVO NEW ZEALAND SUMMIT 2020</footer>
  <footer class="folio folio-right">BRAVO NEW ZEALAND SUMMIT 2020<span class="sep"></span>3</footer>
</main>
</body>
</html>
```